Bref créative
Fire sprinkler company stationary
Halbrook Automatic Sprinkler Co.
Simple
Trent Okafor
President
2745 Pelling Street, Knoxville, TN 37921
contact@halbrooksprinkler.example
The logo to use on the stationary.

```html
<!DOCTYPE html>
<html lang="en">
<head>
<meta charset="utf-8">
<title>Halbrook Automatic Sprinkler Co. — Business Card</title>
<link href="https://fonts.googleapis.com/css2?family=Michroma&family=Montserrat:wght@400;500&display=swap" rel="stylesheet">
<style>
  :root {
    --backdrop: #e9e7e3;
    --card: #ffffff;
    --ink: #1d1d1d;
    --ink-soft: #5a5a5a;
    --icon: #3a3a3a;
    --edge: rgba(0,0,0,0.10);
  }
  * { margin: 0; padding: 0; box-sizing: border-box; }
  html, body {
    width: 1200px; height: 629px; overflow: hidden;
    background: var(--backdrop);
  }
  .stage {
    width: 1200px; height: 629px;
    display: flex; align-items: center; justify-content: center; gap: 60px;
  }
  .card {
    width: 520px; height: 297px;
    background: var(--card);
    box-shadow: 0 2px 10px var(--edge);
    position: relative;
  }
  .brand {
    display: flex; align-items: center; gap: 12px;
    font-family: "Michroma", sans-serif;
    color: var(--ink);
    text-transform: uppercase;
  }
  .brand-mark {
    flex: none; background: var(--ink);
  }
  .brand-name { line-height: 1.35; }

  /* front */
  .card-front { display: flex; align-items: center; justify-content: center; }
  .card-front .brand-mark { width: 46px; height: 46px; }
  .card-front .brand-name { font-size: 19px; }
  .card-front .brand-name span { display: block; font-size: 12px; letter-spacing: 0.5px; }

  /* back */
  .card-back .brand { position: absolute; left: 34px; top: 40px; }
  .card-back .brand-mark { width: 32px; height: 32px; }
  .card-back .brand-name { font-size: 14px; }
  .card-back .brand-name span { display: block; font-size: 9px; }

  .person {
    position: absolute; left: 34px; top: 150px;
    font-family: "Michroma", sans-serif; color: var(--ink);
  }
  .person-name { font-size: 13px; font-variant: small-caps; letter-spacing: 1px; }
  .person-role { font-family: "Montserrat", sans-serif; font-size: 9px; color: var(--ink-soft); margin-top: 4px; }

  .contact {
    position: absolute; right: 30px; top: 140px;
    list-style: none;
    font-family: "Montserrat", sans-serif; font-size: 9.5px; color: var(--ink-soft);
  }
  .contact li { display: flex; align-items: center; gap: 7px; margin-bottom: 8px; }
  .contact svg { width: 13px; height: 13px; flex: none; }

  .address {
    position: absolute; left: 34px; bottom: 26px;
    font-family: "Montserrat", sans-serif; font-size: 9px; letter-spacing: 1.5px; color: var(--ink-soft);
  }
</style>
</head>
<body>
<main class="stage">
  <section class="card card-front">
    <div class="brand">
      <div class="brand-mark"></div>
      <div class="brand-name">Halbrook<span>Automatic Sprinkler Co.</span></div>
    </div>
  </section>

  <section class="card card-back">
    <div class="brand">
      <div class="brand-mark"></div>
      <div class="brand-name">Halbrook<span>Automatic Sprinkler Co.</span></div>
    </div>

    <div class="person">
      <p class="person-name">Trent Okafor</p>
      <p class="person-role">President</p>
    </div>

    <ul class="contact">
      <li>
        <svg viewBox="0 0 16 16"><circle cx="8" cy="8" r="8" fill="var(--icon)"/><path d="M5.5 4.5l1.5 0 .6 2-1 .8a6 6 0 0 0 2.1 2.1l.8-1 2 .6 0 1.5c-3.5.3-6.3-2.5-6-6z" fill="#fff"/></svg>
        865-555-0142
      </li>
      <li>
        <svg viewBox="0 0 16 16"><circle cx="8" cy="8" r="8" fill="var(--icon)"/><rect x="4" y="5.2" width="8" height="5.6" fill="none" stroke="#fff" stroke-width="1"/><path d="M4 5.4l4 3 4-3" fill="none" stroke="#fff" stroke-width="1"/></svg>
        contact@halbrooksprinkler.example
      </li>
      <li>
        <svg viewBox="0 0 16 16"><circle cx="8" cy="8" r="8" fill="var(--icon)"/><circle cx="8" cy="8" r="4" fill="none" stroke="#fff" stroke-width="1"/><path d="M4 8h8M8 4c-2 2.4-2 5.6 0 8M8 4c2 2.4 2 5.6 0 8" fill="none" stroke="#fff" stroke-width="0.8"/></svg>
        halbrooksprinkler.example
      </li>
    </ul>

    <p class="address">2745 Pelling Street, Knoxville, TN 37921</p>
  </section>
</main>
</body>
</html>
```